CPA Firm Business Card
Halvorin, Bestwick & Pardue CPAs, LLC
Project: CPA Firm Business Card
CPA Firm Business Card - Financial Services
Creative Brief
Professional
Moss Brandley, CPA
2867 E. Sable Way, Suite 348 Tucson, AZ 85619
moss@quillledger.net
In addition to business cards design I would also like to see designs for letterheads, envelopes and fax cover sheets.

```html
<!DOCTYPE html>
<html lang="en">
<head>
<meta charset="utf-8">
<title>Halvorin, Bestwick &amp; Pardue CPAs, LLC — Business Card</title>
<link href="https://fonts.googleapis.com/css2?family=Roboto+Condensed:ital,wght@0,400;0,700;1,700&display=swap" rel="stylesheet">
<style>
  :root {
    --bg: #e4e4e4;
    --card: #ffffff;
    --wine: #7a1518;
    --wine-dark: #5e0f12;
    --grey: #8a8a8a;
    --grey-light: #c9c9c9;
    --ink: #4a4a4a;
  }
  * { margin: 0; padding: 0; box-sizing: border-box; }
  html, body { width: 1200px; height: 864px; overflow: hidden; }
  body {
    background: var(--bg);
    font-family: "Roboto Condensed", sans-serif;
    display: flex; flex-direction: column; align-items: center; justify-content: center;
    gap: 28px;
  }
  .card {
    position: relative;
    width: 680px; height: 389px;
    background: var(--card);
    border-radius: 18px;
    overflow: hidden;
    box-shadow: 0 6px 18px rgba(0,0,0,.15);
  }
  /* front */
  .front-mark {
    position: absolute; left: 0; right: 0; top: 120px;
    text-align: center;
    font-size: 104px; font-weight: 700; color: var(--wine);
    letter-spacing: -2px; line-height: 1;
  }
  .front-web {
    position: absolute; left: 0; right: 0; top: 248px;
    text-align: center; font-size: 15px; letter-spacing: 3px; color: var(--ink);
  }
  /* back */
  .swoosh { position: absolute; inset: 0; }
  .firm-name {
    position: absolute; left: 70px; top: 92px; width: 330px;
    font-size: 30px; font-weight: 700; line-height: 1.02;
    text-transform: uppercase; color: var(--wine);
  }
  .firm-rule {
    position: absolute; left: 70px; top: 226px; width: 300px; height: 2px;
    background: var(--grey);
  }
  .person {
    position: absolute; left: 190px; top: 246px;
    font-size: 19px; font-weight: 700; font-style: italic; color: var(--wine);
  }
  .contacts {
    position: absolute; left: 440px; top: 86px; list-style: none;
  }
  .contacts li {
    display: flex; align-items: center; gap: 9px;
    font-size: 14px; color: var(--ink); height: 22px;
  }
  .contacts .dot {
    width: 12px; height: 12px; border-radius: 50%; background: var(--wine); flex: none;
  }
  .contacts .dot.blank { background: transparent; }
</style>
</head>
<body>
  <section class="card card-front">
    <div class="front-mark">HBP</div>
    <div class="front-web">www.hbpllc.com</div>
  </section>

  <section class="card card-back">
    <svg class="swoosh" width="680" height="389" viewBox="0 0 680 389" aria-hidden="true">
      <path d="M0,250 C210,300 430,318 680,292 L680,389 L0,389 Z" fill="var(--grey-light)"/>
      <path d="M0,268 C220,322 420,330 680,312 L680,389 L0,389 Z" fill="var(--grey)"/>
      <path d="M0,282 C190,340 380,372 560,389 L0,389 Z" fill="var(--wine)"/>
    </svg>
    <div class="firm-name">Halvorin, Bestwick &amp; Pardue CPAs, LLC</div>
    <div class="firm-rule"></div>
    <div class="person">Moss Brandley, CPA</div>
    <ul class="contacts">
      <li><span class="dot"></span>2867 E. Sable Way, Suite 348</li>
      <li><span class="dot blank"></span>Tucson, AZ 85619</li>
      <li><span class="dot"></span>520.555.0148</li>
      <li><span class="dot"></span>520.555.0149</li>
      <li><span class="dot"></span>moss@quillledger.net</li>
      <li><span class="dot"></span>www.quillledger.net</li>
    </ul>
  </section>
</body>
</html>
```